Quillo Business Card Design

Looking for elegant and super stylish business cards. Enclosed is the card design we are using now. We need something more contemporary.

Target Market(s)

We are a catering company focusing on weddings and corporate events.

Industry/Entity Type

Caterer

Contact Information for Business Card

Please use similar font to our current cards

Colors
0592cd

Requirements
Must have
• Color and be very unique. Also, please use logo (with or without the castle.)

```html
<!DOCTYPE html>
<html lang="en">
<head>
<meta charset="utf-8">
<title>Quillo Business Card</title>
<link rel="stylesheet" href="https://fonts.googleapis.com/css2?family=Arimo:wght@400;700&display=swap">
<style>
  :root {
    --brand-blue: #0592cd;
    --brand-blue-deep: #0a7db3;
    --ink: #111111;
    --card-white: #ffffff;
    --card-shade: #e6e6e6;
    --stage: #2b2b2b;
    --rule: #333333;
  }
  * { box-sizing: border-box; margin: 0; padding: 0; }
  html, body {
    width: 1200px; height: 997px; overflow: hidden;
    background: var(--stage);
    font-family: "Arimo", Arial, sans-serif;
    color: var(--ink);
  }
  .sheet {
    position: relative; width: 1200px; height: 997px;
    display: flex; align-items: center; justify-content: center; gap: 40px;
  }
  .card {
    position: relative; width: 520px; height: 300px;
    border-radius: 16px; overflow: hidden;
  }
  /* Back of card */
  .card--back {
    background: linear-gradient(160deg, #1aa3dc 0%, var(--brand-blue) 55%, var(--brand-blue-deep) 100%);
    display: flex; align-items: center; justify-content: center;
  }
  .lockup { display: flex; align-items: center; gap: 16px; }
  .lockup__square { background: var(--ink); flex: none; }
  .lockup__name {
    font-weight: 400; color: var(--ink); letter-spacing: 0.04em;
    text-transform: uppercase; line-height: 1;
  }
  .lockup__tagline {
    font-weight: 400; color: var(--ink); letter-spacing: 0.32em;
    text-transform: uppercase; line-height: 1.25;
  }
  .card--back .lockup__square { width: 92px; height: 92px; }
  .card--back .lockup__name { font-size: 46px; }
  .card--back .lockup__tagline { font-size: 15px; margin-top: 6px; }

  /* Front of card */
  .card--front {
    background: linear-gradient(180deg, var(--card-white) 0%, #f7f7f7 60%, var(--card-shade) 100%);
  }
  .card--front .lockup { position: absolute; left: 40px; top: 32px; gap: 10px; }
  .card--front .lockup__square { width: 56px; height: 56px; }
  .card--front .lockup__name { font-size: 28px; }
  .card--front .lockup__tagline { font-size: 9.5px; letter-spacing: 0.3em; margin-top: 3px; }
  .header-rule {
    position: absolute; left: 282px; right: 24px; top: 84px;
    height: 1px; background: var(--rule);
  }
  .person { position: absolute; left: 40px; top: 150px; width: 460px; }
  .person__name {
    display: flex; align-items: flex-end; gap: 8px;
    font-size: 16px; font-weight: 700; color: var(--brand-blue);
  }
  .person__name::after {
    content: ""; flex: 1; height: 1px; background: var(--rule); margin-bottom: 4px;
  }
  .person__title { font-size: 13px; margin-top: 1px; }
  .contacts { list-style: none; margin-top: 16px; }
  .contacts li {
    display: flex; align-items: center; gap: 8px;
    font-size: 14px; line-height: 1; margin-bottom: 9px;
  }
  .contacts svg { width: 14px; height: 14px; flex: none; }
  .address {
    position: absolute; right: 24px; top: 172px;
    text-align: right; font-size: 12px; line-height: 1.3;
  }
  .footer-bands { position: absolute; left: 0; bottom: 0; width: 520px; height: 72px; }
  .website {
    position: absolute; right: 24px; bottom: 16px;
    font-size: 12.5px; font-weight: 700; color: var(--card-white);
  }
</style>
</head>
<body>
<main class="sheet">
  <section class="card card--back" aria-label="Card back">
    <div class="lockup">
      <span class="lockup__square"></span>
      <div>
        <div class="lockup__name">The Quillo</div>
        <div class="lockup__tagline">Catering &amp;<br>Event Design</div>
      </div>
    </div>
  </section>

  <section class="card card--front" aria-label="Card front">
    <div class="lockup">
      <span class="lockup__square"></span>
      <div>
        <div class="lockup__name">The Quillo</div>
        <div class="lockup__tagline">Catering &amp;<br>Event Design</div>
      </div>
    </div>
    <div class="header-rule"></div>

    <div class="person">
      <div class="person__name">Maren Castell</div>
      <div class="person__title">Chief Executive Officer</div>
      <ul class="contacts">
        <li>
          <svg viewBox="0 0 14 14" aria-hidden="true"><circle cx="7" cy="7" r="7" fill="var(--brand-blue)"/><path d="M4.5 3.5h1.6l.6 1.8-1 .7a5 5 0 0 0 2.3 2.3l.7-1 1.8.6v1.6c0 .4-.4.8-.8.8A6 6 0 0 1 3.7 4.3c0-.4.4-.8.8-.8z" fill="#fff"/></svg>
          555 210 4836&nbsp;&nbsp;ext 402
        </li>
        <li>
          <svg viewBox="0 0 14 14" aria-hidden="true"><circle cx="7" cy="7" r="7" fill="var(--brand-blue)"/><rect x="4.6" y="3" width="4.8" height="8" rx="1" fill="#fff"/><rect x="5.4" y="4" width="3.2" height="4.6" fill="var(--brand-blue)"/></svg>
          555 318 2470
        </li>
        <li>
          <svg viewBox="0 0 14 14" aria-hidden="true"><circle cx="7" cy="7" r="7" fill="var(--brand-blue)"/><rect x="3.5" y="4.5" width="7" height="5" fill="#fff"/><path d="M3.5 4.5 7 7.3l3.5-2.8" fill="none" stroke="var(--brand-blue)" stroke-width="0.9"/></svg>
          m@thequillocatering.com
        </li>
      </ul>
    </div>

    <address class="address" style="font-style:normal">4120 Harbor Lane, Ridgeview<br>California 90210</address>

    <svg class="footer-bands" viewBox="0 0 520 72" aria-hidden="true">
      <path d="M0 62 H300 C322 62 326 28 350 28 H520 V72 H0 Z" fill="var(--brand-blue)"/>
      <path d="M0 56 H294 C314 56 318 26 340 24" fill="none" stroke="var(--ink)" stroke-width="5"/>
    </svg>
    <div class="website">www.thequillocatering.com</div>
  </section>
</main>
</body>
</html>
```